Cosmetic injections clinic needs a fresh looking business card

We need a business card using the supplied logo and color scheme to attract future clients to our clinic. It should be modern and fresh, eye catching and not too busy. Simple and to the point is best. I would like two sided designs with the front indicating address and contact information, and the back in full color with white logo and descriptive information also provided.
Target Market(s)
Clients looking for non surgical beauty enhancements.
Contact Information for Business Card
MeloraSkin
14, 618 Birchmont Way
Harwick, Ontario
K2P 7W3
Phone: 587-412-6630
Email: info@meloraskin.com
Requirements
Must have
- -Logo supplied with the name and address of the clinic
- -Back of card in full color with white logo with A small line of text indicating both of the following: Anti aging consultants and cosmetic injectables
- Located inside the Voyager Wellness Group

```html
<!DOCTYPE html>
<html lang="en">
<head>
<meta charset="utf-8">
<title>MeloraSkin Business Card</title>
<link href="https://fonts.googleapis.com/css2?family=Arimo:wght@400;700&display=swap" rel="stylesheet">
<style>
  :root {
    --stage: #2e2e30;
    --purple: #6b3aa3;
    --purple-deep: #5a2d8e;
    --magenta: #b8357a;
    --teal: #2e9487;
    --white: #ffffff;
    --paper: #f4f4f4;
    --ink-soft: #e9e2f3;
  }
  * { margin: 0; padding: 0; box-sizing: border-box; }
  html, body {
    width: 1200px;
    height: 997px;
    overflow: hidden;
    background: var(--stage);
    font-family: "Arimo", Arial, sans-serif;
  }
  .canvas {
    position: relative;
    width: 1200px;
    height: 997px;
  }
  .card {
    position: absolute;
    left: 280px;
    width: 640px;
    height: 366px;
    border-radius: 22px;
    overflow: hidden;
  }

  /* Back of card */
  .card-back {
    top: 90px;
    background: linear-gradient(135deg, #7b49b4 0%, var(--purple) 45%, var(--purple-deep) 100%);
  }
  .card-back .brand {
    position: absolute;
    left: 0;
    right: 0;
    top: 138px;
    display: flex;
    align-items: center;
    justify-content: center;
    gap: 16px;
  }
  .card-back .brand-dot {
    width: 56px;
    height: 56px;
    border-radius: 50%;
    background: var(--white);
  }
  .card-back .brand-name {
    font-weight: 700;
    font-size: 52px;
    color: var(--white);
    letter-spacing: 1px;
  }
  .card-back .tagline {
    position: absolute;
    left: 0;
    right: 0;
    bottom: 26px;
    text-align: center;
    font-size: 13px;
    color: var(--ink-soft);
    letter-spacing: 0.3px;
  }

  /* Front of card */
  .card-front {
    top: 540px;
    background: var(--paper);
  }
  .card-front svg.panels {
    position: absolute;
    inset: 0;
  }
  .card-front .brand {
    position: absolute;
    left: 160px;
    top: 70px;
    display: flex;
    align-items: center;
    gap: 14px;
  }
  .card-front .brand-dot {
    width: 50px;
    height: 50px;
    border-radius: 50%;
    background: var(--purple);
  }
  .card-front .brand-name {
    font-weight: 700;
    font-size: 46px;
    color: var(--magenta);
    letter-spacing: 0.5px;
  }
  .contact {
    position: absolute;
    color: var(--white);
    font-size: 15px;
    line-height: 1.35;
    display: flex;
    flex-direction: column;
    align-items: center;
    text-align: center;
  }
  .contact .icon {
    width: 24px;
    height: 24px;
    margin-bottom: 8px;
  }
  .contact-phone { left: 0; width: 213px; top: 266px; }
  .contact-email { left: 213px; width: 214px; top: 222px; }
  .contact-address { left: 427px; width: 213px; top: 176px; }
</style>
</head>
<body>
<main class="canvas">

  <section class="card card-back" aria-label="Business card back">
    <div class="brand">
      <span class="brand-dot" aria-hidden="true"></span>
      <span class="brand-name">MeloraSkin</span>
    </div>
    <p class="tagline">Anti aging consultants and cosmetic injectables. Located inside the Voyager Wellness Group.</p>
  </section>

  <section class="card card-front" aria-label="Business card front">
    <svg class="panels" width="640" height="366" viewBox="0 0 640 366" aria-hidden="true">
      <rect x="0" y="0" width="213" height="366" fill="var(--purple)"/>
      <rect x="213" y="0" width="214" height="366" fill="var(--magenta)"/>
      <rect x="427" y="0" width="213" height="366" fill="var(--teal)"/>
      <path d="M0 0 H640 V118 Q430 200 213 212 Q90 220 0 236 Z" fill="var(--paper)"/>
    </svg>

    <div class="brand">
      <span class="brand-dot" aria-hidden="true"></span>
      <span class="brand-name">MeloraSkin</span>
    </div>

    <div class="contact contact-phone">
      <svg class="icon" viewBox="0 0 24 24" aria-hidden="true">
        <circle cx="12" cy="12" r="12" fill="rgba(255,255,255,0.85)"/>
        <path d="M7 9.5 Q7 8 9 8 H15 Q17 8 17 9.5 V10.5 H14.5 V9.5 H9.5 V10.5 H7 Z M8.5 11.5 H15.5 L16.5 16 H7.5 Z" fill="var(--purple)"/>
      </svg>
      <span>587-412-6630</span>
    </div>

    <div class="contact contact-email">
      <svg class="icon" viewBox="0 0 24 24" aria-hidden="true">
        <circle cx="12" cy="12" r="12" fill="rgba(255,255,255,0.85)"/>
        <path d="M7 9.5 Q7 8 9 8 H15 Q17 8 17 9.5 V10.5 H14.5 V9.5 H9.5 V10.5 H7 Z M8.5 11.5 H15.5 L16.5 16 H7.5 Z" fill="var(--magenta)"/>
      </svg>
      <span>info@meloraskin.com</span>
    </div>

    <div class="contact contact-address">
      <svg class="icon" viewBox="0 0 24 24" aria-hidden="true">
        <circle cx="12" cy="12" r="12" fill="rgba(255,255,255,0.85)"/>
        <rect x="6.5" y="8" width="11" height="8" fill="none" stroke="var(--teal)" stroke-width="1.4"/>
        <path d="M6.5 8 L12 12.5 L17.5 8" fill="none" stroke="var(--teal)" stroke-width="1.4"/>
      </svg>
      <span>14, 618 Birchmont Way</span>
      <span>Harwick, Ontario, K2P 7W3</span>
    </div>
  </section>

</main>
</body>
</html>
```